Bus Bench Ad Design Needed

Hi there. We would like to design an eye catching bus bench ad! The information that we would like to have on it is found below:

- Our logo which is attached below. We would this to take up at least half of the bus bench.
- Our phone number in bold, very visible to see. 555-318-2694. White numbers on an eye catching colored background.
- Our web address : www.SplitEase472.example
- A "Ring Otto" phrase in a black circle with yellow bold letters. Want the "Ring Otto" to be somewhat angled. We are thinking that the "Ring Otto" should be directly below the image in our logo.
- Our tag line we want somewhere in here as well which is "Divorce made easy - at a price you'll like!"

```html
<!DOCTYPE html>
<html lang="en">
<head>
<meta charset="utf-8">
<title>SplitEase Bus Bench Ad</title>
<link href="https://fonts.googleapis.com/css2?family=Montserrat:ital,wght@0,400;0,500;0,700;0,800;1,800&display=swap" rel="stylesheet">
<style>
  :root {
    --page: #fdfdfd;
    --panel-light: #f7f7f7;
    --panel-dark: #dedede;
    --brand-blue: #0385c5;
    --ink: #1a1a1a;
    --oval: #17191b;
    --callout: #f3e20a;
    --white: #ffffff;
  }
  html, body {
    margin: 0;
    width: 1200px;
    height: 1200px;
    overflow: hidden;
    background: var(--page);
    font-family: "Montserrat", sans-serif;
  }
  .bench-ad {
    position: absolute;
    left: 52px;
    top: 232px;
    width: 1101px;
    height: 315px;
    background: linear-gradient(90deg, var(--panel-light), var(--panel-dark));
    box-shadow: 0 2px 12px rgba(0,0,0,0.12);
    overflow: hidden;
  }
  .brand-mark {
    position: absolute;
    left: 78px;
    top: 34px;
    width: 70px;
    height: 70px;
    background: var(--brand-blue);
  }
  .brand-divider {
    position: absolute;
    left: 193px;
    top: 41px;
    width: 1px;
    height: 93px;
    background: #8a8a8a;
  }
  .brand-name {
    position: absolute;
    left: 205px;
    top: 30px;
    margin: 0;
    font-weight: 500;
    font-size: 72px;
    line-height: 1;
    letter-spacing: 2px;
    color: var(--brand-blue);
  }
  .brand-descriptor {
    position: absolute;
    left: 207px;
    top: 106px;
    margin: 0;
    font-weight: 400;
    font-size: 29px;
    line-height: 1;
    color: var(--ink);
    letter-spacing: 0.3px;
  }
  .contact-band {
    position: absolute;
    left: 426px;
    top: 156px;
    right: 0;
    height: 103px;
    background: linear-gradient(90deg, rgba(3,133,197,0) 0%, rgba(3,133,197,0.45) 30%, var(--brand-blue) 62%);
  }
  .tagline-strip {
    position: absolute;
    left: 426px;
    top: 259px;
    right: 0;
    height: 37px;
    background: linear-gradient(90deg, rgba(180,205,218,0) 0%, #b8d0dc 20%, #d4d4d4 50%, #dadada 100%);
  }
  .accent-rule {
    position: absolute;
    left: 426px;
    top: 296px;
    right: 0;
    height: 11px;
    background: linear-gradient(90deg, rgba(3,133,197,0) 0%, #5aa8d3 20%, var(--brand-blue) 45%);
  }
  .phone {
    position: absolute;
    right: 51px;
    top: 166px;
    margin: 0;
    font-weight: 800;
    font-size: 53px;
    line-height: 1;
    color: var(--white);
    letter-spacing: 0.5px;
  }
  .phone-rule {
    position: absolute;
    right: 51px;
    top: 218px;
    width: 279px;
    height: 2px;
    background: var(--white);
  }
  .web {
    position: absolute;
    right: 55px;
    top: 225px;
    margin: 0;
    font-weight: 700;
    font-size: 19px;
    line-height: 1;
    color: var(--white);
  }
  .tagline {
    position: absolute;
    right: 55px;
    top: 266px;
    margin: 0;
    font-weight: 500;
    font-size: 19px;
    line-height: 1;
    color: var(--ink);
  }
  .callout {
    position: absolute;
    left: 298px;
    top: 153px;
    width: 188px;
    height: 132px;
  }
</style>
</head>
<body>
  <main class="bench-ad">
    <div class="brand-mark"></div>
    <div class="brand-divider"></div>
    <h1 class="brand-name">SplitEase</h1>
    <p class="brand-descriptor">Non-Lawyer Documents Service</p>

    <div class="contact-band"></div>
    <div class="tagline-strip"></div>
    <div class="accent-rule"></div>

    <svg class="callout" viewBox="0 0 188 132" aria-label="Ring Otto">
      <ellipse cx="94" cy="66" rx="92" ry="63" fill="rgba(0,0,0,0.18)" transform="translate(2 3) rotate(-6 94 66)"/>
      <ellipse cx="94" cy="66" rx="92" ry="63" fill="var(--oval)" transform="rotate(-6 94 66)"/>
      <g transform="rotate(-8 94 66)" font-family="Montserrat, sans-serif" font-weight="800" font-style="italic" font-size="44" fill="var(--callout)" text-anchor="middle">
        <text x="96" y="62">RING</text>
        <text x="100" y="104">OTTO</text>
      </g>
    </svg>

    <p class="phone">555-318-2694</p>
    <div class="phone-rule"></div>
    <p class="web">www.SplitEase472.example</p>
    <p class="tagline">Divorce made easy - at a price you'll like!</p>
  </main>
</body>
</html>
```